Web Design for Small Healthcare Startup

Hello,

We are seeking a Website Design for a healthcare company focusing on mobile vaccinations, employee health and wellness services onsite at businesses, and consulting services relating to Healthcare Entities in WA state. Our company’s mission is to “To aid in a healthier workplace”. Vitality Caravan will provide on-site wellness services to employers that simplify and streamline employee preventative health as well as onsite consulting services to help with compliance of Healthcare Entities.

We are seeking a Website Design for Vitality Caravan, PLLC. Our company’s mission is to provide mobile health and wellness services to employers onsite at their businesses. These services include mobile vaccinations clinics for employees as well as wellness and health screenings. The company will also offer healtcare compliance consulting services for Healthcare Entities. The company was founded to bring these important healthcare services to businesses and keep employees healthy. Healthy employees are the cornerstone to a great business and we want to help orginazations achieve their goals of having a healthy productive workforce.

We are looking for a moderin website design that will need to be coded. We have attached our current logo design for reference as well as a brief questionare regarding our business for your information (not necessary to include all information). We would like something SEO friendly and easy to navigate.

Thank you!

Vitality Caravan, PLLC

Target Market(s)

Small Businesses

Industry/Entity Type

Healthcare

Coding

Coded - Design and coding required

Number of Pages Required

1 page

Requirements
Nice to have
• SEO Friendly, Incorporate Logo

```html
<!DOCTYPE html>
<html lang="en">
<head>
<meta charset="utf-8">
<title>Vitality Caravan, PLLC – On-site Mobile Vaccine Clinics</title>
<link rel="stylesheet" href="https://fonts.googleapis.com/css2?family=Poppins:ital,wght@0,400;0,500;0,600;0,700;1,700;1,800&display=swap">
<style>
:root{
  --blue:#124fa3;
  --blue-deep:#0d3f8a;
  --purple:#a2489d;
  --sky:#a9cfe2;
  --sky-light:#d6e9f2;
  --text:#3a3a48;
  --muted:#6b6b78;
  --grey-bg:#f3f3f6;
  --white:#ffffff;
}
*{margin:0;padding:0;box-sizing:border-box}
html,body{width:1200px;height:4100px;overflow:hidden}
body{font-family:"Poppins",sans-serif;color:var(--text);background:var(--white);position:relative}
.abs{position:absolute}
.shapes{position:absolute;left:0;top:0;width:1200px;height:4100px}

/* header */
.site-header{position:absolute;left:0;top:0;width:1200px;height:88px;background:var(--white)}
.brand{position:absolute;left:88px;top:30px;display:flex;align-items:center;gap:8px;font-weight:700;font-size:17px;color:var(--blue)}
.brand-dot{width:14px;height:14px;border-radius:50%;background:var(--purple)}
.main-nav{position:absolute;top:36px;left:0;font-size:14px;font-weight:500;color:#222}
.main-nav a{position:absolute;white-space:nowrap;color:inherit;text-decoration:none}
.main-nav a.active{color:var(--purple)}
.main-nav a.active::before{content:"";position:absolute;left:0;right:0;top:-36px;height:2px;background:var(--purple)}

/* hero */
.hero-kicker{left:148px;top:232px;font-size:18px;font-weight:700;font-style:italic;color:var(--white)}
.hero-kicker::before{content:"";position:absolute;left:-60px;top:11px;width:50px;height:2px;background:var(--white)}
.hero-title{left:88px;top:262px;font-size:72px;line-height:76px;font-weight:800;font-style:italic;color:var(--white);width:520px}
.play-btn{left:992px;top:540px;width:118px;height:118px;border-radius:50%;background:var(--purple);display:flex;align-items:center;justify-content:center}

.reserve{left:0;width:1200px;top:886px;text-align:center;font-size:34px;font-weight:700;font-style:italic;color:var(--blue)}
.reserve span{border-bottom:2px solid var(--blue);padding-bottom:2px}

.section-title{font-size:48px;font-weight:700;font-style:italic;color:var(--blue);line-height:1.1}
.rule-left::before{content:"";position:absolute;left:-28px;bottom:-2px;width:70px;height:2px;background:#c9c9d3}

/* about */
.about-title{left:602px;top:1096px}
.about-copy{left:601px;top:1174px;width:510px;font-size:14.5px;line-height:20px;color:var(--text)}
.about-copy p{margin-bottom:13px}

/* services */
.services-title{left:88px;top:1572px}
.service-list{left:86px;top:1650px;width:540px;list-style:none;font-size:14.5px;line-height:20px}
.service-list li{position:relative;padding-left:18px;margin-bottom:12px}
.service-list li::before{content:"";position:absolute;left:0;top:5px;width:10px;height:10px;border-radius:50%;background:var(--blue)}
.btn-pill{left:86px;top:1986px;width:165px;height:41px;border-radius:21px;background:var(--purple);color:var(--white);font-size:10px;font-weight:700;display:flex;align-items:center;justify-content:center}

/* schedule */
.center-title{left:0;width:1200px;text-align:center}
.subtitle{left:0;width:1200px;text-align:center;font-size:14.5px;color:var(--text)}
.step-num{font-size:66px;font-weight:800;color:#e9e9ee;width:200px;text-align:center;top:2366px}
.step-label{width:150px;text-align:center;font-size:12.5px;font-weight:600;line-height:15px;color:#1e1e2a}

.divider{left:88px;top:2754px;width:1023px;height:1px;background:#e1e1e8}

/* pricing */
.price-card{background:var(--white);border-radius:14px;box-shadow:0 6px 24px rgba(30,40,80,.08);text-align:center;padding:38px 22px 0}
.price-card.featured{border:4px solid var(--purple)}
.price-step{font-size:19px;font-weight:700;color:var(--blue)}
.price-card.featured .price-step{color:var(--purple)}
.price-head{margin-top:14px;font-size:12.5px;font-weight:600;line-height:18px;color:#1e1e2a;min-height:60px}
.price-card hr{border:0;border-top:1px solid #e4e4ea;margin:6px 0 28px}
.price-note{font-size:13px;line-height:21px;color:var(--muted)}

/* cta */
.cta{left:139px;top:3359px;width:923px;height:205px;border-radius:103px;background:var(--purple)}
.cta-text{left:108px;top:46px;font-size:42px;line-height:54px;font-weight:800;font-style:italic;color:var(--white)}
.cta-btn{left:633px;top:81px;width:184px;height:44px;border-radius:22px;background:var(--white);font-size:11px;font-weight:700;color:#1e1e2a;display:flex;align-items:center;justify-content:center}

/* footer */
.foot-brand{left:150px;top:3815px;display:flex;align-items:center;gap:8px;font-size:19px;font-weight:700;color:var(--white)}
.socials{left:124px;top:3893px;display:flex;gap:10px}
.socials span{width:42px;height:42px;border-radius:50%;background:rgba(255,255,255,.14)}
.foot-head{font-size:20px;font-weight:700;font-style:italic;color:var(--white);top:3744px}
.foot-links{left:384px;top:3796px;list-style:none;font-size:12.5px;color:var(--white)}
.foot-links li{height:31.4px}
.foot-links li::before{content:"›";margin-right:8px}
.contact-item{left:568px;font-size:12.5px;line-height:18px;color:var(--white);padding-left:22px;width:220px}
.contact-item svg{position:absolute;left:0;top:2px}
.news-copy{left:817px;top:3794px;width:240px;font-size:12.5px;line-height:18px;color:var(--white)}
.news-input{left:817px;top:3853px;width:258px;height:44px;border-radius:22px;background:var(--white);font-size:12px;color:#8a8a96;display:flex;align-items:center;padding-left:38px}
.foot-rule{left:0;top:4036px;width:1200px;height:1px;background:rgba(255,255,255,.25)}
.copyright{left:0;width:1200px;top:4058px;text-align:center;font-size:12.5px;color:var(--white)}
.to-top{left:1131px;top:4014px;width:44px;height:44px;border-radius:50%;background:var(--purple);display:flex;align-items:center;justify-content:center}
</style>
</head>
<body>

<svg class="shapes" viewBox="0 0 1200 4100" aria-hidden="true">
  <!-- hero backdrop -->
  <path d="M0 88H1200V470C1120 560 1050 640 920 700C820 750 720 770 560 730C420 700 300 580 180 620C100 650 40 640 0 620Z" fill="var(--sky)"/>
  <!-- services grey band -->
  <path d="M0 2050C150 2200 330 2210 520 2150C760 2080 980 2070 1200 2000V2900H0Z" fill="var(--grey-bg)"/>
  <rect x="0" y="2560" width="1200" height="200" fill="var(--grey-bg)"/>
  <rect x="0" y="2756" width="1200" height="740" fill="var(--white)"/>
  <!-- footer wave -->
  <path d="M0 3460C150 3620 330 3700 520 3640C760 3560 980 3460 1200 3520V4100H0Z" fill="var(--blue)"/>
  <!-- schedule rings -->
  <g fill="none">
    <circle cx="304" cy="2555" r="112" stroke="var(--blue)" stroke-width="2" stroke-dasharray="2 14"/>
    <circle cx="304" cy="2555" r="98" stroke="var(--blue)" stroke-width="8" stroke-dasharray="430 200" transform="rotate(-120 304 2555)"/>
    <circle cx="595" cy="2555" r="112" stroke="var(--purple)" stroke-width="2" stroke-dasharray="2 14"/>
    <circle cx="595" cy="2555" r="98" stroke="var(--purple)" stroke-width="8" stroke-dasharray="430 200" transform="rotate(-120 595 2555)"/>
    <circle cx="890" cy="2555" r="112" stroke="var(--blue)" stroke-width="2" stroke-dasharray="2 14"/>
    <circle cx="890" cy="2555" r="98" stroke="var(--blue)" stroke-width="8" stroke-dasharray="430 200" transform="rotate(-120 890 2555)"/>
    <line x1="420" y1="2555" x2="478" y2="2555" stroke="var(--blue)" stroke-width="2"/>
    <line x1="712" y1="2555" x2="772" y2="2555" stroke="var(--purple)" stroke-width="2"/>
    <circle cx="420" cy="2555" r="6" stroke="var(--blue)" stroke-width="2" fill="#fff"/>
    <circle cx="478" cy="2555" r="6" stroke="var(--purple)" stroke-width="2" fill="#fff"/>
    <circle cx="712" cy="2555" r="6" stroke="var(--purple)" stroke-width="2" fill="#fff"/>
    <circle cx="772" cy="2555" r="6" stroke="var(--blue)" stroke-width="2" fill="#fff"/>
  </g>
  <g fill="#fff" style="filter:drop-shadow(0 4px 10px rgba(0,0,0,.12))">
    <circle cx="304" cy="2555" r="90"/><circle cx="595" cy="2555" r="90"/><circle cx="890" cy="2555" r="90"/>
  </g>
  <!-- step icons -->
  <g fill="none" stroke="var(--blue)" stroke-width="2">
    <rect x="292" y="2500" width="22" height="26" rx="2"/><line x1="297" y1="2508" x2="309" y2="2508"/><line x1="297" y1="2515" x2="309" y2="2515"/>
    <rect x="877" y="2500" width="26" height="24" rx="4"/><circle cx="884" cy="2495" r="4"/><circle cx="896" cy="2495" r="4"/>
  </g>
  <g fill="none" stroke="var(--purple)" stroke-width="2">
    <rect x="578" y="2496" width="34" height="30" rx="3"/><line x1="578" y1="2505" x2="612" y2="2505"/><circle cx="607" cy="2522" r="7" fill="#fff"/>
  </g>
</svg>

<header class="site-header">
  <div class="brand"><span class="brand-dot"></span>Vitality Caravan</div>
  <nav class="main-nav">
    <a class="active" style="left:533px">HOME</a>
    <a style="left:602px">ABOUT US</a>
    <a style="left:697px">SERVICES</a>
    <a style="left:790px">SCHEDULE TODAY</a>
    <a style="left:938px">PRICING</a>
    <a style="left:1020px">CONTACT US</a>
  </nav>
</header>

<div class="abs" role="img" aria-label="Photo of a nurse in gloves vaccinating a smiling masked woman giving a thumbs up"
  style="left:560px;top:88px;width:640px;height:670px;border-radius:0 0 0 60%;background:linear-gradient(150deg,#c7dce6,#8fa3b0 55%,#e7e2dd)"></div>
<p class="abs hero-kicker">Welcome to</p>
<h1 class="abs hero-title">Making the workplace a healthier place...</h1>
<div class="abs play-btn"><svg width="22" height="24" viewBox="0 0 22 24"><path d="M3 2L20 12L3 22Z" fill="#fff"/></svg></div>

<h2 class="abs reserve"><span>Reserve your on-site mobile vaccine clinic today!</span></h2>

<section>
  <div class="abs" role="img" aria-label="Photo of a smiling team of medical staff in scrubs in front of an ambulance"
    style="left:0;top:1016px;width:528px;height:488px;border-radius:20% 75% 60% 10%/25% 60% 70% 30%;background:linear-gradient(135deg,#cfe6f1,#4f8fb0 40%,#c94848 70%,#dcebf2)"></div>
  <h2 class="abs section-title about-title rule-left">About Us</h2>
  <div class="abs about-copy">
    <p>Vitality Caravan, PLLC mission: Making the workplace a healthier place.</p>
    <p>To provide on-sitewellness services to employers that simplify and streamline employee preventative health.</p>
    <p>Pharmacist owned and operated.</p>
    <p>Vitality Caravan, PLLC was started by local, Washington state licensed pharmacist with over 15 years experience vaccinating patients. She is a highly skilled immunizer and enjoys interacting with patients while providing this important preventative health services. Her vaccination experience spans from individual patient vaccinations to large clinics during community outbreaks.</p>
  </div>
</section>

<section>
  <h2 class="abs section-title services-title rule-left">Our Services</h2>
  <ul class="abs service-list">
    <li>Vitality Caravan will come to you!</li>
    <li>No crowded waiting rooms, no long lines, no hassle!</li>
    <li>Hassle-free, streamlining the vaccination process … provide this on-site service as part of your employee wellness package</li>
    <li>Serving employers who want to increase the health and Wellness of their workplace</li>
    <li>Vaccines including seasonal flu, COVID,Pneumonia</li>
    <li>Ensure your employees and their families remain healthy this flu season. Host a flu shot clinic on site to help your employees get vaccinated. Provide this service as part of youremployeeWellness benefits package.</li>
    <li>Vitality Caravan specializes in providing seamless, hassle-free vaccine clinics.</li>
  </ul>
  <div class="abs btn-pill">READ MORE SERVICE</div>
  <div class="abs" role="img" aria-label="Photo of a man receiving a vaccine injection in his upper arm"
    style="left:724px;top:1525px;width:494px;height:494px;border-radius:50%;background:linear-gradient(135deg,#7cc3e8,#5aa9d6 50%,#c89a7a)"></div>
  <div class="abs" role="img" aria-label="Photo of rows of small vaccine vials"
    style="left:682px;top:1882px;width:212px;height:212px;border-radius:50%;border:8px solid #fff;box-shadow:0 10px 30px rgba(0,0,0,.15);background:radial-gradient(circle,#f4f6f9,#c9d2e2)"></div>
</section>

<section>
  <h2 class="abs section-title center-title" style="top:2252px">Schedule Today</h2>
  <p class="abs subtitle" style="top:2328px">Hassle-free, streamlining the vaccination process ...</p>
  <span class="abs step-num" style="left:204px">01</span>
  <span class="abs step-num" style="left:492px">02</span>
  <span class="abs step-num" style="left:790px">03</span>
  <p class="abs step-label" style="left:229px;top:2546px">Submit Vaccine Clinic Needs Questionnaire.</p>
  <p class="abs step-label" style="left:520px;top:2539px">Vitality Caravan, PLLC will contact you to schedule on-site vaccine clinic.</p>
  <p class="abs step-label" style="left:815px;top:2539px">Prepare your employees for vaccine clinic day.</p>
</section>

<div class="abs divider"></div>

<section>
  <h2 class="abs section-title center-title" style="top:2806px">Our Pricing</h2>
  <p class="abs subtitle" style="top:2882px">Hassle-free, streamlining the vaccination process ...</p>
  <div class="abs price-card" style="left:200px;top:2956px;width:252px;height:296px">
    <p class="price-step">STEP 1</p>
    <p class="price-head">Submit Vaccine Clinic Needs Questionnaire.</p><hr>
    <p class="price-note">Price quote is simple! No hidden travel/mileage calculations, no hidden hourly fees.</p>
  </div>
  <div class="abs price-card featured" style="left:456px;top:2939px;width:288px;height:332px;padding-top:52px">
    <p class="price-step">STEP 2</p>
    <p class="price-head">Vitality Caravan, PLLC will contact you to schedule on-site vaccine clinic.</p><hr>
    <p class="price-note">Price quote is simple! No hidden travel/mileage calculations, no hidden hourly fees.</p>
  </div>
  <div class="abs price-card" style="left:748px;top:2956px;width:252px;height:296px">
    <p class="price-step">STEP 3</p>
    <p class="price-head">Prepare your employees for vaccine clinic day.</p><hr>
    <p class="price-note">Price quote is simple! No hidden travel/mileage calculations, no hidden hourly fees.</p>
  </div>
</section>

<div class="abs cta">
  <p class="abs cta-text">Start building your<br>event today with me!</p>
  <div class="abs cta-btn">MY EVENT PLANNER</div>
</div>

<footer>
  <div class="abs foot-brand"><span class="brand-dot" style="background:#fff"></span>Vitality Caravan</div>
  <div class="abs socials"><span></span><span></span><span></span><span></span></div>

  <h3 class="abs foot-head" style="left:384px">Quick links</h3>
  <ul class="abs foot-links">
    <li>Home</li><li>About Us</li><li>Services</li><li>Schedule Today</li><li>Pricing</li><li>Contact Us</li>
  </ul>

  <h3 class="abs foot-head" style="left:568px">Contact info</h3>
  <div class="abs contact-item" style="top:3794px">
    <svg width="14" height="11" viewBox="0 0 14 11"><rect x="1" y="1" width="12" height="9" fill="none" stroke="#fff" stroke-width="1.5"/><path d="M1 1L7 6L13 1" fill="none" stroke="#fff" stroke-width="1.5"/></svg>
    Email:<br>hello@vitalitycaravan.example</div>
  <div class="abs contact-item" style="top:3848px">
    <svg width="14" height="14" viewBox="0 0 14 14"><path d="M3 1L6 4L4.5 6C5.5 8 6 8.5 8 9.5L10 8L13 11L11 13C6 13 1 8 1 3Z" fill="#fff"/></svg>
    Phone:<br>+1 360 555 0142</div>
  <div class="abs contact-item" style="top:3902px">
    <svg width="12" height="16" viewBox="0 0 12 16"><path d="M6 1C3 1 1 3 1 6C1 10 6 15 6 15S11 10 11 6C11 3 9 1 6 1Z" fill="#fff"/><circle cx="6" cy="6" r="2" fill="var(--blue)"/></svg>
    Location:<br>214 Harbor Lane,<br>Olympia WA</div>

  <h3 class="abs foot-head" style="left:817px">Newsletter</h3>
  <p class="abs news-copy">Subscribe to our email address to get the latest news.</p>
  <div class="abs news-input">Enter Your Email...
    <svg class="abs" style="left:14px;top:16px" width="13" height="11" viewBox="0 0 13 11"><rect x="1" y="1" width="11" height="9" fill="none" stroke="#9a9aa6" stroke-width="1.3"/></svg>
    <svg class="abs" style="left:224px;top:14px" width="16" height="16" viewBox="0 0 16 16"><path d="M1 8L15 1L11 15L8 9Z" fill="var(--purple)"/></svg>
  </div>

  <div class="abs foot-rule"></div>
  <p class="abs copyright">© Copyright 2022 VitalityCaravan PLLC, All Rights Reserved</p>
  <div class="abs to-top"><svg width="12" height="14" viewBox="0 0 12 14"><path d="M6 13V2M1 6L6 1L11 6" fill="none" stroke="#fff" stroke-width="1.6"/></svg></div>
</footer>

</body>
</html>
```